Flu Brochure- brief and easy-to-read

A team of health educators is looking to design a brochure on what Americans need to "know and do" when it comes to flu season. All copy and images will be provided.

The brochure needs to be an 8.5 x 11 inch bi-fold design.

I am only able to upload up to 5 files. So, additional images will have to sent via dropbox or some other mechanism.

Target Market(s)

The audience is vast, but the content and design need to be simple and engaging.

Industry/Entity Type

Health

Requirements
Must have
• Must Have:
- Clear and Simple, Easy-to-read and Understand and Act on- should be very focused on what the consumer should do about taking care of themselves when it comes to the flu.

We will provide all of the copy for the brochure design. We will also provide photographs for the project.

Captions for photographs that support the key message.

Should Not Have:
- x reverse print- e.g., no white font on a black background
x fancy fonts or heavy use of italics
x use of all capitals
x no full justification
x no use of drop caps

Must be multicultural as well.

```html
<!DOCTYPE html>
<html lang="en">
<head>
<meta charset="utf-8">
<title>Flu – Know and Do brochure</title>
<link rel="stylesheet" href="https://fonts.googleapis.com/css2?family=Arimo:wght@400;700&family=Josefin+Sans:wght@300&display=swap">
<style>
  :root {
    --page-bg: #ececec;
    --paper: #ffffff;
    --blue-deep: #1b75bb;
    --blue-light: #29a8e0;
    --blue-faint: #d3e3f1;
    --ink: #1f1f1f;
    --sponsor-red: #c8102e;
    --kids-a: #e9c3a6;
    --kids-b: #7fa86a;
    --sick-a: #d9d4cc;
    --sick-b: #8d7f74;
  }
  html, body {
    margin: 0;
    width: 1200px;
    height: 960px;
    overflow: hidden;
    background: var(--page-bg);
  }
  .brochure {
    position: absolute;
    left: 5px;
    top: 95px;
    width: 1190px;
    height: 770px;
    background: var(--paper);
    font-family: "Arimo", Arial, sans-serif;
    color: var(--ink);
    box-shadow: 0 6px 20px rgba(0,0,0,.18);
    overflow: hidden;
  }
  .shapes { position: absolute; inset: 0; }
  .display-title {
    position: absolute;
    margin: 0;
    font-family: "Josefin Sans", "Century Gothic", sans-serif;
    font-weight: 300;
    line-height: 1;
  }
  .back-title {
    left: 0; top: 32px;
    font-size: 82px;
    line-height: 87px;
    color: var(--blue-faint);
  }
  .front-title {
    left: 1033px; top: 74px;
    font-size: 43px;
    line-height: 44px;
    color: var(--blue-deep);
  }
  .resources {
    position: absolute;
    left: 103px; top: 663px;
    width: 400px;
    text-align: center;
    color: #fff;
    font-size: 15px;
    line-height: 19px;
    margin: 0;
  }
  .question {
    position: absolute;
    left: 620px; top: 403px;
    width: 545px;
    text-align: center;
    font-size: 24px;
    line-height: 32px;
    margin: 0;
  }
  .actions {
    position: absolute;
    left: 700px; top: 520px;
    display: grid;
    grid-template-columns: 196px 200px;
    row-gap: 6px;
    margin: 0; padding: 0;
    list-style: none;
  }
  .action {
    display: flex;
    align-items: center;
    gap: 14px;
    font-size: 35px;
    font-weight: 700;
    color: var(--blue-deep);
    line-height: 40px;
  }
  .action svg { flex: none; }
  .credits {
    position: absolute;
    left: 645px; top: 651px;
    width: 515px;
    font-size: 11px;
    line-height: 14px;
    margin: 0;
  }
  .sponsor {
    position: absolute;
    left: 743px; top: 712px;
    width: 300px; height: 46px;
    box-sizing: border-box;
    border: 1.5px solid var(--blue-deep);
    border-radius: 12px;
    display: flex;
    align-items: center;
    justify-content: center;
    gap: 12px;
  }
  .sponsor-label { font-size: 11px; }
  .sponsor-name { font-size: 22px; font-weight: 700; color: var(--sponsor-red); }
</style>
</head>
<body>
<main class="brochure">
  <svg class="shapes" width="1190" height="770" viewBox="0 0 1190 770">
    <defs>
      <linearGradient id="kids-tone" x1="0" y1="0" x2="1" y2="1">
        <stop offset="0" stop-color="var(--kids-a)"/>
        <stop offset="1" stop-color="var(--kids-b)"/>
      </linearGradient>
      <linearGradient id="sick-tone" x1="0" y1="0" x2="1" y2="1">
        <stop offset="0" stop-color="var(--sick-a)"/>
        <stop offset="1" stop-color="var(--sick-b)"/>
      </linearGradient>
    </defs>
    <!-- back panel -->
    <polygon points="177,0 595,0 595,178" fill="var(--blue-deep)"/>
    <polygon class="photo-kids" points="150,205 540,205 540,449 70,687 70,290 150,290" fill="url(#kids-tone)" role="img" aria-label="Photo of four smiling children leaning in together"/>
    <polygon points="0,723 595,421 595,770 0,770" fill="var(--blue-light)"/>
    <polygon points="0,768 595,438 595,770" fill="var(--blue-deep)"/>
    <!-- front panel -->
    <polygon class="photo-sick" points="595,0 1190,0 1190,215 1015,330 840,278 595,173" fill="url(#sick-tone)" role="img" aria-label="Photo of a woman with the flu blowing her nose and holding a thermometer"/>
    <polygon points="595,178 825,273 595,421" fill="var(--blue-light)"/>
    <polygon points="1190,215 1015,330 1190,403" fill="var(--blue-light)"/>
    <polyline points="595,433 840,278 1190,418" fill="none" stroke="var(--blue-deep)" stroke-width="8"/>
  </svg>

  <h2 class="display-title back-title">KNOW<br>AND<br>DO</h2>
  <p class="resources">For reliable info on flu:<br>Call your doctor<br>Go to: http://www.fluready.example/flu/<br>Call 1-800-555-0142</p>

  <h1 class="display-title front-title">KNOW<br>AND<br>DO</h1>
  <p class="question">FLU<br>What are 4 things I can do to prepare for<br>the flu season and keep my family healthy?</p>
  <ul class="actions">
    <li class="action"><svg width="16" height="22" viewBox="0 0 16 22"><path d="M3 2 L13 11 L3 20" fill="none" stroke="var(--ink)" stroke-width="4"/></svg>Know</li>
    <li class="action"><svg width="16" height="22" viewBox="0 0 16 22"><path d="M3 2 L13 11 L3 20" fill="none" stroke="var(--ink)" stroke-width="4"/></svg>Protect</li>
    <li class="action"><svg width="16" height="22" viewBox="0 0 16 22"><path d="M3 2 L13 11 L3 20" fill="none" stroke="var(--ink)" stroke-width="4"/></svg>Prevent</li>
    <li class="action"><svg width="16" height="22" viewBox="0 0 16 22"><path d="M3 2 L13 11 L3 20" fill="none" stroke="var(--ink)" stroke-width="4"/></svg>Treat</li>
  </ul>
  <p class="credits">©2013. Riverside Health Literacy Team. Riverside University. Marlow L, Kestrel KJ, Avery RT. Content based on scientific evidence from the N.H.D. and the National Disease Prevention Office (NDPO) as of March 2013.</p>
  <div class="sponsor">
    <span class="sponsor-label">Sponsored by:</span>
    <span class="sponsor-name">Harlow &amp; Pine</span>
  </div>
</main>
</body>
</html>
```